I need a business card for myself, being a proprietor of a funeral parlor based in Manila. I'd like the card to have either of the following:
White Font on Black Background
or
Black Font on White Background
No logo is needed however I will appreciate any efforts to show a symbol of eternal happiness, aptly designed with above mentioned colors in mind.
Company name, address and contact on the lower right corner.
Logo or symbol anywhere.
Quillstone Funeral Services
+639174826351
darvik4521@pelmora.com
corner of Brisco Avenue and Velhurst Street
Makati City, Philippines
Thank you.
Update: Please include a small dove in your design. You are free to choose where you would like it on the card.

```html
<!DOCTYPE html>
<html lang="en">
<head>
<meta charset="utf-8">
<title>Quillstone Funeral Services – Business Cards</title>
<link href="https://fonts.googleapis.com/css2?family=Cinzel:wght@400;700&display=swap" rel="stylesheet">
<style>
  :root {
    --backdrop: #e4e4e4;
    --paper: #f2f2f1;
    --ink: #2b2b2b;
    --onyx-top: #2c2c2d;
    --onyx-bottom: #1b1b1c;
    --wine-top: #8c2b31;
    --wine-bottom: #701418;
    --icon-fill: #ffffff;
  }
  * { box-sizing: border-box; margin: 0; padding: 0; }
  html, body {
    width: 1200px;
    height: 720px;
    overflow: hidden;
    background: var(--backdrop);
  }
  .stage {
    position: relative;
    width: 1200px;
    height: 720px;
  }
  .card {
    position: absolute;
    top: 242px;
    width: 420px;
    height: 240px;
    background: var(--paper);
    overflow: hidden;
    font-family: "Cinzel", serif;
  }
  .card--onyx { left: 147px; }
  .card--wine { left: 633px; }

  .card__art {
    position: absolute;
    inset: 0;
    width: 420px;
    height: 240px;
  }
  .card__name {
    position: absolute;
    left: 18px;
    right: 239px;
    top: 113px;
    color: #ffffff;
    font-weight: 700;
    font-size: 9.5px;
    line-height: 12px;
    letter-spacing: 0;
    text-align: right;
    white-space: nowrap;
  }
  .card__detail {
    position: absolute;
    left: 244px;
    right: 12px;
    color: var(--ink);
    font-size: 10px;
    line-height: 12px;
  }
  .card__detail--phone { top: 72px; }
  .card__detail--email { top: 114px; text-transform: lowercase; }
  .card__detail--address { top: 148px; }
</style>
</head>
<body>
<main class="stage">

  <article class="card card--onyx">
    <svg class="card__art" viewBox="0 0 420 240" aria-hidden="true">
      <defs>
        <linearGradient id="onyx-panel" x1="0" y1="0" x2="0" y2="1">
          <stop offset="0" stop-color="#2c2c2d"/>
          <stop offset="1" stop-color="#1b1b1c"/>
        </linearGradient>
      </defs>
      <rect class="panel" x="0" y="0" width="232" height="240" fill="url(#onyx-panel)"/>
      <polygon class="edge-notch" points="0,105 14,120 0,135" fill="var(--backdrop)"/>
      <g class="divider-tabs" fill="var(--paper)">
        <polygon points="232,69 219,80 232,91"/>
        <polygon points="232,109 219,120 232,131"/>
        <polygon points="232,150 219,161 232,172"/>
      </g>
      <g class="icon icon--phone" transform="translate(198 78)">
        <circle r="11" fill="var(--icon-fill)"/>
        <path d="M-5,-4.5 l2.5,-1.8 2,3.4 -1.6,1.2 c0.8,1.8 1.8,2.8 3.6,3.6 l1.2,-1.6 3.4,2 -1.8,2.5 c-5,0 -9.3,-4.3 -9.3,-9.3z" fill="var(--onyx-bottom)"/>
      </g>
      <g class="icon icon--mail" transform="translate(198 120)">
        <circle r="11" fill="var(--icon-fill)"/>
        <rect x="-5.5" y="-3.8" width="11" height="7.6" fill="var(--onyx-bottom)"/>
        <path d="M-5.5,-3.8 L0,0.8 L5.5,-3.8" fill="none" stroke="#ffffff" stroke-width="0.9"/>
      </g>
      <g class="icon icon--pin" transform="translate(198 161)">
        <circle r="11" fill="var(--icon-fill)"/>
        <path d="M0,7 C-2,3.5 -4.5,0.5 -4.5,-2.2 A4.5,4.5 0 0 1 4.5,-2.2 C4.5,0.5 2,3.5 0,7z" fill="var(--onyx-bottom)"/>
        <circle cy="-2.3" r="1.6" fill="#ffffff"/>
      </g>
    </svg>
    <h1 class="card__name">Quillstone Funeral Services</h1>
    <p class="card__detail card__detail--phone">+639174826351</p>
    <p class="card__detail card__detail--email">darvik4521@pelmora.com</p>
    <p class="card__detail card__detail--address">corner of Brisco Avenue and<br>Velhurst Street Makati City,<br>Philippines</p>
  </article>

  <article class="card card--wine">
    <svg class="card__art" viewBox="0 0 420 240" aria-hidden="true">
      <defs>
        <linearGradient id="wine-panel" x1="0" y1="0" x2="0" y2="1">
          <stop offset="0" stop-color="#8c2b31"/>
          <stop offset="1" stop-color="#701418"/>
        </linearGradient>
      </defs>
      <rect class="panel" x="0" y="0" width="232" height="240" fill="url(#wine-panel)"/>
      <polygon class="edge-notch" points="0,105 14,120 0,135" fill="var(--backdrop)"/>
      <g class="divider-tabs" fill="var(--paper)">
        <polygon points="232,69 219,80 232,91"/>
        <polygon points="232,109 219,120 232,131"/>
        <polygon points="232,150 219,161 232,172"/>
      </g>
      <g class="icon icon--phone" transform="translate(198 78)">
        <circle r="11" fill="var(--icon-fill)"/>
        <path d="M-5,-4.5 l2.5,-1.8 2,3.4 -1.6,1.2 c0.8,1.8 1.8,2.8 3.6,3.6 l1.2,-1.6 3.4,2 -1.8,2.5 c-5,0 -9.3,-4.3 -9.3,-9.3z" fill="var(--wine-bottom)"/>
      </g>
      <g class="icon icon--mail" transform="translate(198 120)">
        <circle r="11" fill="var(--icon-fill)"/>
        <rect x="-5.5" y="-3.8" width="11" height="7.6" fill="var(--wine-bottom)"/>
        <path d="M-5.5,-3.8 L0,0.8 L5.5,-3.8" fill="none" stroke="#ffffff" stroke-width="0.9"/>
      </g>
      <g class="icon icon--pin" transform="translate(198 161)">
        <circle r="11" fill="var(--icon-fill)"/>
        <path d="M0,7 C-2,3.5 -4.5,0.5 -4.5,-2.2 A4.5,4.5 0 0 1 4.5,-2.2 C4.5,0.5 2,3.5 0,7z" fill="var(--wine-bottom)"/>
        <circle cy="-2.3" r="1.6" fill="#ffffff"/>
      </g>
    </svg>
    <h1 class="card__name">Quillstone Funeral Services</h1>
    <p class="card__detail card__detail--phone">+639174826351</p>
    <p class="card__detail card__detail--email">darvik4521@pelmora.com</p>
    <p class="card__detail card__detail--address">corner of Brisco Avenue and<br>Velhurst Street Makati City,<br>Philippines</p>
  </article>

</main>
</body>
</html>
```